General Service Offerings Brochure

We need a general services brochure that describes to our customers-using evocative imagery-what products and services we offer. Our company is called Halvern Supply and it is a spinoff of Marrowfield Systems Corporation (MSC).
We have a logo design that is green and gray which we are very happy with. The brochure needs to persuade clients to call on us for systems integration, professional equipment (through our ecommerce web site), and authorized service on a variety of professional audio/video brands. We build mobile broadcast units, repair these units, and sell a variety of boxed equipment. The brochure content would also be used in an "about us" type page. We need a sharp, professional presentation. Clients are professional engineers and media executives who are spending capital purchasing budgets with us.
The brochure will not usually be printed but sent as an email attachment (pdf) and adapted as an "About Us" web page.

Project Deadline Extended
Reason: provide more time to offer photos and files to designers for submissions

new About Us file uploaded including scrolling text, headline capabilities, and the old About Us bullet points.

Please check files for newest About Us document and place this test into your designs. Thanks

Target Market(s)

Males ages 40-60 who are tech-savvy, web-savvy, professional, and familiar with the industry

Requirements
Must have
• 1-2 pages should probably be enough. Must discuss our primary offerings which are:
1. We design and build ENG and SNG Systems
2. We diagnose and repair ENG and SNG trucks
3. We sell and service professional Halvern Supply

Must use imagery, professional design, be adaptable to web.
Must use existing logo design and colors. Will incorporate other logos from brands we represent.
Nice to have
• A tag phrase or motif would be nice to sum-up our service offerings. We serve mostly broadcasters who are on a bridge to new technology. Our firm offers repairs on "legacy" equipment (the old boring stuff) to help keep customers going. We also, however, offer cutting-edge designs with new satellite news gathering systems.
Should not have
• no Rallex flags, no pet pictures, no turquoise, no tire or wheel graphics. No lightning bolts. Free stock images are fine if appropriate although we should have enough photos to fill the layout. Muted colors that work with the logo are best. Fonts should be up-to-date

```html
<!DOCTYPE html>
<html lang="en">
<head>
<meta charset="utf-8">
<title>Halvern Supply – Service Brochure</title>
<link href="https://fonts.googleapis.com/css2?family=Questrial&family=Montserrat:ital,wght@0,600;0,700;1,600&display=swap" rel="stylesheet">
<style>
:root{
  --canvas:#ffffff;
  --page:#fbfbfb;
  --slate:#4c545c;
  --green:#8ee01e;
  --ink:#5a6168;
  --white:#ffffff;
}
*{margin:0;padding:0;box-sizing:border-box}
html,body{width:1200px;height:823px;overflow:hidden;background:var(--canvas)}
body{position:relative;font-family:"Questrial",sans-serif;color:var(--ink)}
.page{position:absolute;top:50px;width:500px;height:725px;
  background:linear-gradient(180deg,var(--page) 0%,#f3f3f3 100%);
  box-shadow:0 0 3px rgba(0,0,0,.18);overflow:hidden}
.page--front{left:62px}
.page--about{left:598px}
.brand{position:absolute;left:35px;top:25px;display:flex;align-items:center;gap:8px}
.brand__mark{width:14px;height:14px;background:var(--slate)}
.brand__name{font-size:17px;color:var(--slate);line-height:1}
.headline{position:absolute;right:27px;top:42px;text-align:right;color:var(--green);
  font-size:31px;line-height:1.07;font-weight:400}
.page--about .headline{top:38px;right:28px}
.tile{position:absolute;width:215px;height:214px}
.tile--slate{background:var(--slate);color:var(--white)}
.tile--green{background:var(--green);color:var(--white)}
.copy{font-size:8.4px;line-height:1.42;text-align:justify;padding:44px 14px 0 14px}
.copy a{color:var(--white);font-weight:700;text-decoration:none;font-family:"Montserrat",sans-serif}
.copy--right{text-align:right;padding:24px 14px 0 14px}
.wrap-spacer{float:left;width:1px;height:36px}
.photo--dish{float:left;clear:left;width:60px;height:66px;margin:0 8px 0 -14px;border-radius:50% 50% 8px 8px;
  background:radial-gradient(circle at 40% 40%,#f4f4f2,#c9c9c4)}
.claims{list-style:none;padding:26px 12px 0 6px}
.claims li{position:relative;padding-left:16px;margin-bottom:14px;
  font-family:"Montserrat",sans-serif;font-style:italic;font-weight:600;font-size:10.6px;line-height:1.32}
.claims li::before,.bullets li::before{content:"+";position:absolute;left:0;font-style:normal;font-weight:400;font-family:"Questrial",sans-serif}
.claims li::before{color:var(--white);font-size:14px;top:-3px}
.bullets{list-style:none;padding:26px 10px 0 6px}
.bullets li{position:relative;padding-left:14px;margin-bottom:9px;font-size:9.6px;line-height:1.25;text-align:justify}
.tile--slate .bullets li::before{color:var(--green);font-size:13px;top:-3px}
.tile--green .bullets li::before{color:var(--white);font-size:13px;top:-3px}
.photo{position:absolute}
.photo--truck{left:0;top:568px;width:258px;height:145px;
  background:linear-gradient(180deg,#e6e5df 0%,#d4d3cb 60%,#bdbcb4 100%)}
.photo--night{left:252px;top:166px;width:221px;height:214px;
  background:linear-gradient(160deg,#2c2a2e 0%,#5b3a2e 40%,#8b8078 70%,#3a3a3c 100%)}
.photo--pipes{left:34px;top:385px;width:214px;height:214px;
  background:linear-gradient(135deg,#5e6468 0%,#c9ccce 35%,#8d9296 55%,#d6d8da 75%,#6a7074 100%)}
.photo--units{left:0;top:600px;width:225px;height:120px;
  background:linear-gradient(180deg,#c8d8ec 0%,#4a74b8 60%,#dfe8f4 100%)}
.contact{position:absolute;right:29px;top:614px;text-align:right;color:var(--green);font-size:10.2px;line-height:1.12;font-style:normal}
.contact__phone{font-family:"Montserrat",sans-serif;font-weight:700;font-size:14px;margin-top:2px}
.contact__fax{font-size:9.8px}
.contact__web{position:absolute;right:29px;top:678px;font-family:"Montserrat",sans-serif;font-weight:700;font-size:10.4px;color:var(--slate)}
.partners{position:absolute;right:28px;top:663px;display:flex;gap:12px;align-items:center}
</style>
</head>
<body>

<section class="page page--front">
  <div class="brand"><span class="brand__mark"></span><span class="brand__name">Halvern Supply</span></div>
  <h1 class="headline">Crossing the Bridge<br>to New Workflow</h1>

  <div class="tile tile--slate" style="left:33px;top:166px">
    <p class="copy">Here at Halvern Supply our specialty is building trucks for remote broadcasting. Our industry is on a “bridge” to new territory—using new means and methods of transmitting live video. Our mission is to help broadcasters cross the bridge by maintaining legacy equipment while deploying new workflows as well. We offer full service repairs and systems replacement on ENG/SNG trucks including masts, generators, flexcoil assemblies, HD Video Systems, and our HD Skyward mast camera.</p>
  </div>
  <div class="tile tile--slate" style="left:252px;top:166px;width:219px">
    <p class="copy" style="padding-top:40px">When it comes to new designs we specialize in agile, affordable ENG and DSNG systems using compact vehicles with new power solutions. We offer legacy platforms like Hauler 350 and Courier for long-range, long-term live shots. We manufacture the HD Skyward mast camera system for crisp images of breaking news from the mast top perspective. Our legacy RL-20B helps secure a reliable link between the truck and studio during a live shot. We ship professional broadcast equipment worldwide from our website at <a>www.halvernsupply.com</a></p>
  </div>
  <div class="tile tile--slate" style="left:33px;top:385px">
    <p class="copy copy--right"><span class="wrap-spacer"></span><span class="photo--dish" role="img" aria-label="Satellite dish on the vehicle roof"></span>Our industry is on a bridge to new territory. Whether we are working with a fleet or a single truck—our specialty is to help our customers manage both legacy and emerging technology for maximum coverage. Whether you need a mast overhaul, a new SNG truck, or have questions about an HD upgrade—we stand ready to leverage our experience.</p>
  </div>
  <div class="tile tile--green" style="left:252px;top:385px;width:219px">
    <ul class="claims">
      <li>We design, build, and service ENG/SNG Trucks and Fly-Away Systems</li>
      <li>We design and install hardware and workflow upgrades to ENG/SNG fleets</li>
      <li>We ship and support professional broadcast equipment worldwide</li>
    </ul>
  </div>

  <div class="photo photo--truck" role="img" aria-label="White SUV news vehicle with a roof-mounted satellite dish"></div>

  <address class="contact">
    1420 Ridgeway Works Lane<br>Fenwick, MO 63999<br>United States
    <div class="contact__phone">(888) 555-0142</div>
    <div class="contact__fax">Fax: (888) 555-0187</div>
  </address>
  <div class="contact__web">www.HalvernSupply.com</div>
</section>

<section class="page page--about">
  <div class="brand"><span class="brand__mark"></span><span class="brand__name">Halvern Supply</span></div>
  <h1 class="headline">About Us</h1>

  <div class="tile tile--slate" style="left:34px;top:166px;width:214px">
    <ul class="bullets">
      <li>Full service design/build/repair on ENG and DSNG trucks and Fly-Away Systems</li>
      <li>Supplier of professional broadcast equipment and consulting</li>
      <li>Specialists in HD System Conversion and Fleet Planning</li>
      <li>Centrally located in Fenwick, Missouri</li>
      <li>Repeat customers include Tolland Broadcast, Northlight Media, Brennard Communications, Ashby Media</li>
    </ul>
  </div>
  <div class="photo photo--night" role="img" aria-label="Broadcast trucks with raised masts at a night-time news scene"></div>
  <div class="photo photo--pipes" role="img" aria-label="Technician inspecting telescoping mast sections in the workshop"></div>
  <div class="tile tile--green" style="left:252px;top:385px;width:221px">
    <ul class="bullets">
      <li>Authorized Service Center for Ardent Power, VEPS, Ridgeline Masts, Tallbrook Masts, Pivotline Quick-Mount</li>
      <li>Specialists in Digital Satellite News Gathering (DSNG) workflow, integration, and training</li>
      <li>Manufacturers of the HD Skyward mast camera system and RL-20B.</li>
      <li>Emergency Service Facility for ENG truck masts, generators, and RF Systems</li>
      <li>Specialists in Flexcoil cable assemblies and installation</li>
    </ul>
  </div>
  <div class="photo photo--units" role="img" aria-label="Stack of blue and white rack-mount fiber transmission units"></div>

  <div class="partners" aria-label="Partner brands">
    <svg width="210" height="26" viewBox="0 0 210 26" aria-hidden="true">
      <rect x="0" y="7" width="44" height="12" fill="#2a2a2a"/>
      <rect x="56" y="7" width="44" height="12" fill="#9a9a9a"/>
      <circle cx="126" cy="13" r="13" fill="#1f4fa0"/>
      <rect x="160" y="3" width="44" height="20" fill="#2a2a2a"/>
    </svg>
  </div>
</section>

</body>
</html>
```